Awesome law firm seeks great artwork for sign to be installed at local roller skating rink!!

We're a dynamic, law firm that does its work with a difference - we actually care about our clients and our fees are usually lower than most other firms.

We are installing a sign that's 78cm (height) x 158cm (width) to be printed on 3mm Aluminum Composite Panel and installed at a local roller skating rink in Kalamunda, Perth, Western Australia.

Graphics need to be provided in vector .eps (Encapsulated Post Script), .ai (Adobe Illustrator) or PDF format.

We have uploaded a copy of our Logo, which should feature on the sign (we usually have it on the top right of our stationery, but are happy to see other suggestions), together with our practice areas - Family Law, Wills and Estates, Building and Construction, Corporate and Commercial, Local Government, General legal (personal or business).

We don't have a 'slogan' for our firm, but for the roller skating rink sign, we're thinking of something like 'We roll with you", or something similar. Surprise us :)

Sign should also indicate that our team are local to "the Hills", which is how this area (the Kalamunda and surrounding areas of Perth) is known.

Main colors of the sign can include blue, white, black and red (more blue, white and black preferred).

The final design should communicate trust and expertise in law, but have a fun edge (the sign's at a roller skating rink after all and will be seen on every lap as it's in the rink).

The sign must include our website address www.venkarilegal.com (note this is still under construction in case you google us :)), our phone number 0431 508 279 and our main email address, which is admin@venkarilegal.com

Beyond this, we're happy to see any cool ideas for the design of our sign.

Target Market(s)

Local families and business owners at local roller skating rink

Industry/Entity Type

Legal services

Font styles to use
Serif
Other font styles liked:
• Designer to choose

Colors
0054AA
0677BA
7BADD7
CADEEF
E8F1F8
EB3D1F
EC4F4E
F09395
F8D3D4
FCEDEE

Requirements
Must have
• Logo, contact details, design as per description and can have the words "Get your skates on!"
Nice to have
• Awesome, striking, appealing design - easy to read as you're zooming past on your skates!
Should not have
• Any offensive, explicit, corny or suggestive words and preferably avoid cliché rhyming catch phrases, albeit we do want something fun that has a skating vibe

```html
<!DOCTYPE html>
<html lang="en">
<head>
<meta charset="utf-8">
<title>Venkari Legal – Rink Sign</title>
<link rel="stylesheet" href="https://fonts.googleapis.com/css2?family=Arimo:wght@400;700&family=Tinos:wght@700&display=swap">
<style>
  :root{
    --ink:#000000;
    --paper:#ffffff;
    --brand-blue:#4472c4;
    --backdrop:#e9edf2;
  }
  *{margin:0;padding:0;box-sizing:border-box;}
  html,body{width:1200px;height:1041px;overflow:hidden;background:var(--backdrop);}
  .sign{position:absolute;left:20px;top:234px;width:1160px;height:573px;background:var(--paper);overflow:hidden;font-family:"Arimo",Arial,sans-serif;}
  .sign__dark{position:absolute;left:0;top:0;width:670px;height:573px;background:var(--ink);}
  .slogan{position:absolute;color:var(--paper);line-height:1;}
  .slogan--we{left:48px;top:72px;font-size:60px;letter-spacing:-2px;}
  .slogan--roll{position:absolute;top:54px;color:var(--brand-blue);font-weight:700;font-size:142px;line-height:1;letter-spacing:-4px;}
  .slogan--ro{left:160px;}
  .slogan--l{left:532px;}
  .skate-art{position:absolute;left:408px;top:0;width:116px;height:168px;background:linear-gradient(180deg,#4472c4 0%,#3d66b0 100%);border-radius:0 0 14px 14px;}
  .slogan--with{left:162px;top:186px;font-size:62px;letter-spacing:-1px;}
  .practice{position:absolute;left:69px;top:300px;border-left:6px solid var(--brand-blue);padding-left:20px;color:var(--paper);list-style:none;}
  .practice li{font-size:26px;line-height:37px;white-space:nowrap;}
  .practice small{font-size:14px;margin-left:6px;}
  .firm-name{position:absolute;left:774px;top:80px;color:var(--brand-blue);font-family:"Tinos","Times New Roman",serif;font-weight:700;font-size:62px;line-height:1.15;letter-spacing:2px;}
  .contact-icon{position:absolute;width:66px;height:66px;border-radius:50%;background:var(--brand-blue);}
  .contact-icon svg{position:absolute;left:15px;top:15px;}
  .contact-icon--phone{left:642px;top:342px;}
  .contact-icon--web{left:642px;top:428px;}
  .phone{position:absolute;left:725px;top:340px;font-size:66px;color:var(--ink);letter-spacing:1px;}
  .web{position:absolute;left:734px;top:418px;font-size:29px;font-weight:700;line-height:36px;color:var(--ink);}
</style>
</head>
<body>
<main class="sign">
  <section class="sign__dark">
    <span class="slogan slogan--we">WE</span>
    <span class="slogan--roll slogan--ro">RO</span>
    <div class="skate-art" role="img" aria-label="Illustrated leg wearing an inline roller skate, standing in as the first letter L"></div>
    <span class="slogan--roll slogan--l">L</span>
    <span class="slogan slogan--with">WITH YOU....</span>
    <ul class="practice">
      <li>FAMILY LAW</li>
      <li>WILLS AND ESTATES</li>
      <li>BUILDING AND CONSTRUCTION</li>
      <li>CORPORATE AND COMMERCIAL</li>
      <li>LOCAL GOVERNMENT</li>
      <li>GENERAL LEGAL<small>(PERSONAL OR BUSINESS)</small></li>
    </ul>
  </section>
  <h1 class="firm-name">VENKARI<br>LEGAL</h1>
  <div class="contact-icon contact-icon--phone">
    <svg width="36" height="36" viewBox="0 0 24 24" fill="none" stroke="#fff" stroke-width="1.8" stroke-linecap="round" stroke-linejoin="round" aria-hidden="true">
      <path d="M22 16.9v3a2 2 0 0 1-2.2 2 19.8 19.8 0 0 1-8.6-3.1 19.5 19.5 0 0 1-6-6A19.8 19.8 0 0 1 2.1 4.2 2 2 0 0 1 4.1 2h3a2 2 0 0 1 2 1.7c.1.9.4 1.8.7 2.7a2 2 0 0 1-.5 2.1L8 9.8a16 16 0 0 0 6 6l1.3-1.3a2 2 0 0 1 2.1-.4c.9.3 1.8.6 2.7.7a2 2 0 0 1 1.7 2z"/>
      <path d="M15 5a5 5 0 0 1 4 4M15 1a9 9 0 0 1 8 8"/>
    </svg>
  </div>
  <p class="phone">0431 508 279</p>
  <div class="contact-icon contact-icon--web">
    <svg width="36" height="36" viewBox="0 0 24 24" fill="none" stroke="#fff" stroke-width="1.8" aria-hidden="true">
      <circle cx="12" cy="12" r="10"/>
      <ellipse cx="12" cy="12" rx="4.5" ry="10"/>
      <path d="M2 12h20M4 7h16M4 17h16"/>
    </svg>
  </div>
  <p class="web">www.venkarilegal.com<br>admin@venkarilegal.com</p>
</main>
</body>
</html>
```